Cosmetic Dentist Practice needs stationery package/logo

I need a letterhead, envelope and business card for a cosmetic and Dental Inplant practice in an upscale part of Houston. The business card will be a size 3.5 x 2 and the letterhead will be 8.5" x 11" with a standard #10 envelope.
I have uploaded a file with an idea that the dentist had for his cards. Please note that this is not the size that the card should be. It does provide the information required.
Updates
Thank you all for your submissions. They were each unique and special in their own way. My client has made a selection that he feels best meets his needs. I appreciate each of you taking the time to offer designs. Good luck to each of you...I hope to see you back in MarblePost on future projects.
Industry/Entity Type
Business
Look and feel
Each slider illustrates characteristics of the customer's brand and the style your logo design should communicate.

```html
<!DOCTYPE html>
<html lang="en">
<head>
<meta charset="utf-8">
<title>Midtown Aesthetic &amp; Implant Dental — Business Card</title>
<link rel="stylesheet" href="https://fonts.googleapis.com/css2?family=Alegreya+Sans:wght@700&family=Arimo:wght@400&family=Roboto+Condensed:wght@400&display=swap">
<style>
  :root {
    --ink: #1c1c1c;
    --ink-soft: #2a2a2a;
    --paper-top: #ffffff;
    --paper-mid: #ebebeb;
    --band-mid: #5a5a5a;
    --band-dark: #000000;
    --light-text: #ffffff;
  }
  html, body {
    margin: 0;
    padding: 0;
    width: 1200px;
    height: 700px;
    overflow: hidden;
    background: #ffffff;
  }
  .business-card {
    position: relative;
    width: 1200px;
    height: 700px;
    background: linear-gradient(180deg,
      var(--paper-top) 0%,
      var(--paper-mid) 55%,
      #cfcfcf 63%,
      var(--band-mid) 75%,
      #141414 89%,
      var(--band-dark) 100%);
    overflow: hidden;
  }
  .practice-name {
    position: absolute;
    margin: 0;
    font-family: "Alegreya Sans", sans-serif;
    font-weight: 700;
    color: var(--ink);
    font-size: 62px;
    line-height: 1;
    white-space: nowrap;
  }
  .practice-name--first { left: 54px; top: 62px; }
  .practice-name--second { left: 232px; top: 170px; }

  .dentist {
    position: absolute;
    left: 0;
    width: 1220px;
    top: 328px;
    text-align: center;
  }
  .dentist-name {
    margin: 0;
    font-family: "Alegreya Sans", sans-serif;
    font-weight: 700;
    font-size: 46px;
    line-height: 1;
    color: var(--ink);
  }
  .dentist-title {
    margin: 8px 0 0;
    font-family: "Arimo", sans-serif;
    font-size: 40px;
    line-height: 1;
    color: var(--ink-soft);
  }
  .dentist-email {
    margin: 10px 0 0;
    font-family: "Arimo", sans-serif;
    font-size: 28px;
    line-height: 1;
    color: var(--ink-soft);
  }
  .office-address {
    position: absolute;
    left: 41px;
    top: 554px;
    margin: 0;
    font-family: "Arimo", sans-serif;
    font-style: normal;
    font-size: 33px;
    line-height: 34px;
    color: var(--light-text);
  }
  .office-lines {
    position: absolute;
    right: 48px;
    top: 558px;
    margin: 0;
    font-family: "Roboto Condensed", sans-serif;
    font-size: 46px;
    line-height: 50px;
    color: var(--light-text);
  }
</style>
</head>
<body>
  <main class="business-card">
    <h1 class="practice-name practice-name--first">Midtown Aesthetic</h1>
    <p class="practice-name practice-name--second">&amp; Implant Dental</p>

    <section class="dentist">
      <p class="dentist-name">Daniel Marsh, D.D.S., PLLC</p>
      <p class="dentist-title">Prosthodontist</p>
      <p class="dentist-email">DrMarsh@maidtx.com</p>
    </section>

    <address class="office-address">
      72 Cedar Ridge Lane<br>
      Suite 210 W<br>
      Houston, TX 77019
    </address>

    <p class="office-lines">
      Phone: 713.555.0142<br>
      Fax: 713.555.0187
    </p>
  </main>
</body>
</html>
```